Vexla.IO Portal Application Design

** See the attached treatment PDF document with complete details, but here are the broad points:**

We need designs for a login screen and three very similar interior page screens. Because the app requires a CodeNest, RepoDen or Pailforge account to login, screen shots are attached to this treatment. Please review those for the designs needed.
- Login Page
- Project Index page (with sidebar tabs for other options. Those specific pages do not need to be coded once we have the template).
- Project build list. A list of the builds available per project
- Build details. This shows the build steps and results of the build steps.

The site should be visually compatible with https://vexlasite.examplehost.net. The same logo and color scheme (logo attached)

General templates are desired that we can build on.

There is a significant bonus tip involved if you’re willing to provide a toggle for a light and a dark mode. I do not know what this would look like but feel free to present proposals.

Industry/Entity Type

Continuous Integration/Testing (think LoopRun, MarlowCI)

Coding

Coded - Design and coding required

Number of Pages Required

1 page

Font styles to use
Sans Serif
Other font styles liked:
• Roboto

Colors
0054AA
0677BA
7BADD7
CADEEF
E8F1F8
FFC000
F8CF3A
FAE287
FDF2CF
FEFAEE

Requirements
Nice to have
• Light and Dark Mode

```html
<!DOCTYPE html>
<html lang="en">
<head>
<meta charset="utf-8">
<title>Vexla.IO – Sign in</title>
<link rel="stylesheet" href="https://fonts.googleapis.com/css2?family=Roboto:wght@300;400;500&family=Roboto+Condensed:wght@700&display=swap">
<style>
  :root {
    --page-bg: #323a58;
    --card-bg: #373e5b;
    --card-border: #4b5273;
    --brand-text: #a9a7b9;
    --brand-dot: #a9a7b9;
    --intro-text: #eceaf2;
    --button-bg: #a3a1b3;
    --button-hover-start: #f4f4f7;
    --button-hover-end: #aeacbd;
    --button-text: #1a1c28;
    --icon-dot: #2a2f47;
    --server-icon: #4a1530;
    --link-text: #d4d2de;
  }
  * { box-sizing: border-box; margin: 0; padding: 0; }
  html, body {
    width: 1200px;
    height: 1200px;
    overflow: hidden;
    background: var(--page-bg);
    font-family: "Roboto", sans-serif;
  }
  .login-card {
    position: absolute;
    left: 402px;
    top: 308px;
    width: 394px;
    height: 456px;
    background: var(--card-bg);
    border: 1px solid var(--card-border);
    border-radius: 26px;
  }
  .brand {
    position: absolute;
    left: 82px;
    top: 48px;
    display: flex;
    align-items: center;
    gap: 20px;
  }
  .brand-mark {
    width: 56px;
    height: 56px;
    border-radius: 50%;
    background: var(--brand-dot);
  }
  .brand-name {
    font-family: "Roboto Condensed", "Roboto", sans-serif;
    font-weight: 700;
    font-size: 50px;
    line-height: 1;
    color: var(--brand-text);
  }
  .intro {
    position: absolute;
    left: 73px;
    top: 131px;
    width: 250px;
    font-size: 11px;
    font-weight: 500;
    line-height: 13px;
    color: var(--intro-text);
  }
  .provider-list {
    position: absolute;
    left: 66px;
    top: 210px;
    width: 259px;
    list-style: none;
    display: flex;
    flex-direction: column;
    gap: 21px;
  }
  .provider-button {
    display: flex;
    align-items: center;
    justify-content: center;
    gap: 9px;
    height: 31px;
    border-radius: 16px;
    background: var(--button-bg);
    color: var(--button-text);
    font-size: 11px;
    font-weight: 500;
    text-decoration: none;
  }
  .provider-button.is-hovered {
    background: linear-gradient(90deg, var(--button-hover-start), var(--button-hover-end));
  }
  .provider-dot {
    width: 20px;
    height: 20px;
    border-radius: 50%;
    background: var(--icon-dot);
  }
  .server-icon { width: 20px; height: 14px; }
  .footer-links {
    position: absolute;
    top: 801px;
    left: 0;
    width: 1200px;
    font-size: 10.5px;
    font-weight: 300;
  }
  .footer-link {
    position: absolute;
    color: var(--link-text);
    text-decoration: none;
  }
  .footer-link.support { left: 516px; }
  .footer-link.help { left: 617px; }
  .footer-link svg { width: 7px; height: 7px; margin-left: 3px; vertical-align: -1px; }
</style>
</head>
<body>
  <main class="login-card">
    <div class="brand">
      <span class="brand-mark" aria-hidden="true"></span>
      <span class="brand-name">Vexla.IO</span>
    </div>
    <p class="intro">Lorem ipsum dolor sit amet, consectetuer adipiscing elit, sed diam nonummy nibh euismod</p>
    <ul class="provider-list">
      <li><a class="provider-button is-hovered" href="#"><span class="provider-dot"></span>Sign in with CodeNest</a></li>
      <li><a class="provider-button" href="#"><span class="provider-dot"></span>Sign in with Pailforge</a></li>
      <li><a class="provider-button" href="#"><span class="provider-dot"></span>Sign in with RepoDen</a></li>
      <li><a class="provider-button" href="#">
        <svg class="server-icon" viewBox="0 0 20 14" aria-hidden="true">
          <rect x="1" y="1" width="18" height="4.5" rx="2.2" fill="none" stroke="var(--server-icon)" stroke-width="1.6"/>
          <rect x="1" y="8.5" width="18" height="4.5" rx="2.2" fill="none" stroke="var(--server-icon)" stroke-width="1.6"/>
          <circle cx="4" cy="3.25" r="0.9" fill="var(--server-icon)"/>
          <circle cx="4" cy="10.75" r="0.9" fill="var(--server-icon)"/>
        </svg>
        Sign in with a self-hosted service</a></li>
    </ul>
  </main>
  <nav class="footer-links">
    <a class="footer-link support" href="#">Support<svg viewBox="0 0 7 7" aria-hidden="true"><path d="M1 6 L6 1 M2.5 1 H6 V4.5" fill="none" stroke="currentColor" stroke-width="0.9"/></svg></a>
    <a class="footer-link help" href="#">Help Center<svg viewBox="0 0 7 7" aria-hidden="true"><path d="M1 6 L6 1 M2.5 1 H6 V4.5" fill="none" stroke="currentColor" stroke-width="0.9"/></svg></a>
  </nav>
</body>
</html>
```